Flyer-Design für Immobilienmakler
Zielgruppe
Immobilienmakler. Zielgruppe: Hausverkäufer im mittleren und älteren Alter.
Aufgabenstellung
Textvorschlag:
Eine kostenlose Immobilienbewertung bekommen Sie von jedem Makler, wir reduzieren zusätzlich unsere Vermittlungsprovision.
Sparen Sie jetzt 2 %* Provision
Alles wird teurer. Wir reduzieren die Provision!
Wir helfen bei der Verwirklichung Ihres Wohntraums. Angebot gültig gegen Vorlage des Flyers.
*Bei uns 2 % weniger:
• Übliche Maklerprovision 5,95 %
• 3,95 % bedeutet Alleinprovision oder geteilte Provision 1,97 %
• Gilt ab ein Verkaufswert von 400.000,- Euro
• Gültig bis 30. Dezember 2022
• Nur gegen Vorlage des Flyers
und Alleinauftrag.

```html
<!DOCTYPE html>
<html lang="de">
<head>
<meta charset="utf-8">
<title>Velmora GmbH – Flyer Provision</title>
<link rel="stylesheet" href="https://fonts.googleapis.com/css2?family=Archivo+Black&family=Gelasio:wght@500&family=Lato:wght@400;700&family=Roboto:wght@300;400;500;700&display=swap">
<style>
  :root {
    --stage: #4c4b4c;
    --paper: #ffffff;
    --teal: #1b7570;
    --teal-text: #1a6e68;
    --navy: #1c2a33;
    --lime: #9dc544;
    --logo: #36495a;
    --leaf: #4f9a3c;
    --ink: #1b1b1b;
    --muted: #7a7a7a;
  }
  * { box-sizing: border-box; margin: 0; padding: 0; }
  html, body { width: 1200px; height: 800px; overflow: hidden; }
  body { background: var(--stage); position: relative; font-family: "Roboto", Arial, sans-serif; }

  .flyer {
    position: absolute; left: 331px; top: 20px;
    width: 782px; height: 1106px;
    transform: scale(0.687); transform-origin: 0 0;
    background: var(--paper); overflow: hidden;
  }
  .flyer > * { position: absolute; }

  .brand { left: 126px; top: 22px; display: flex; align-items: center; gap: 16px; }
  .brand__mark { width: 40px; height: 40px; background: var(--leaf); }
  .brand__name { font-family: "Gelasio", Georgia, serif; font-weight: 500; font-size: 50px; color: var(--logo); line-height: 1; }
  .tagline { left: 101px; top: 88px; font-size: 28px; color: var(--leaf); letter-spacing: 0.5px; }

  .photo-house { left: 240px; top: 152px; width: 542px; height: 424px;
    background: linear-gradient(180deg, #cfe6f4 0%, #eef3f5 45%, #c9cccd 70%, #6aa33c 85%, #4e8a2b 100%); }
  .photo-frame { left: 0; top: 176px; width: 331px; height: 271px; background: var(--paper);
    border: 1px solid #c9c9c9; border-left: none; box-shadow: 0 4px 10px rgba(0,0,0,0.12); }
  .photo-meeting { left: 14px; top: 19px; width: 300px; height: 233px;
    background: linear-gradient(135deg, #eaeceb 0%, #dfe3e6 40%, #8d96a6 70%, #e6e8ea 100%); }

  .offer { left: 0; top: 447px; width: 240px; height: 130px; background: var(--paper); }
  .offer__lead { position: absolute; left: 30px; top: 20px; font-family: Arial, "Roboto", sans-serif; font-size: 31px; color: var(--ink); }
  .offer__value { z-index: 3; left: 65px; top: 506px; font-family: "Archivo Black", Arial, sans-serif; font-size: 48px; color: var(--teal-text); line-height: 1; }
  .offer__value sup { font-family: Arial, sans-serif; font-size: 26px; color: var(--ink); vertical-align: top; position: relative; top: -4px; }
  .offer__word { z-index: 3; left: 27px; top: 558px; font-family: "Archivo Black", Arial, sans-serif; font-size: 36px; color: var(--teal-text); line-height: 1; }

  .intro { z-index: 1; left: 0; top: 576px; width: 404px; height: 180px; background: var(--paper); padding: 32px 0 0 9px; }
  .intro__claim { font-size: 18px; font-weight: 300; color: var(--teal-text); letter-spacing: 0.4px; white-space: nowrap; }
  .intro__body { margin-top: 6px; font-size: 16px; line-height: 21px; color: var(--ink); letter-spacing: 0.3px; }
  .intro__note { margin-top: 6px; font-family: "Lato", sans-serif; font-size: 16px; color: var(--muted); }

  .photo-dining { left: 0; top: 756px; width: 404px; height: 240px;
    background: linear-gradient(90deg, #e9dcd3 0%, #f3f1ee 18%, #78a86a 35%, #9bc089 55%, #f2efeb 75%, #ece6e0 100%); }

  .valuation { left: 404px; top: 576px; width: 378px; height: 107px; background: var(--navy);
    padding: 22px 0 0 30px; color: #fff; font-family: Arial, "Roboto", sans-serif; font-weight: 700; }
  .valuation__title { font-size: 26px; line-height: 34px; }
  .valuation__region { font-size: 24px; line-height: 34px; }

  .benefits { left: 404px; top: 683px; width: 378px; height: 313px; background: var(--teal);
    color: #fff; font-family: "Lato", sans-serif; padding: 6px 10px 0 39px; }
  .benefits__text { font-size: 19px; line-height: 23px; }
  .benefits__list { list-style: none; margin-top: 14px; }
  .benefits__item { position: relative; padding-left: 42px; font-size: 19px; line-height: 21px; margin-bottom: 21px; }
  .benefits__item::before { content: ""; position: absolute; left: 6px; top: 50%; width: 19px; height: 19px;
    margin-top: -9px; border-radius: 50%; background: #fff; }

  .contact { left: 0; top: 996px; width: 782px; height: 110px; background: var(--lime); color: #fff; }
  .contact__phone-icon { position: absolute; left: 30px; top: 42px; }
  .contact__phone { position: absolute; left: 84px; top: 46px; font-size: 33px; font-weight: 700; letter-spacing: 0.5px; }
  .contact__pin { position: absolute; left: 352px; top: 42px; }
  .contact__address { position: absolute; left: 404px; top: 28px; font-size: 20px; line-height: 23px; letter-spacing: 0.4px; font-weight: 300; font-style: normal; }
</style>
</head>
<body>
  <main class="flyer">
    <div class="brand">
      <span class="brand__mark"></span>
      <span class="brand__name">Velmora GmbH</span>
    </div>
    <p class="tagline">Für zukunftsweisende Werte</p>

    <div class="photo-house" role="img" aria-label="Foto eines modernen weißen Einfamilienhauses mit Terrasse und Rasen"></div>

    <div class="photo-frame">
      <div class="photo-meeting" role="img" aria-label="Foto: Makler berät ein Paar am Schreibtisch"></div>
    </div>

    <div class="offer"><p class="offer__lead">Sparen Sie</p></div>

    <section class="intro">
      <p class="intro__claim">Alles wird teurer. Wir reduzieren die Provision!</p>
      <p class="intro__body">Eine kostenlose Immobilienbewertung<br>bekommen Sie von jedem Makler,<br>Wir reduzieren zusätzlich unsere Vermittlungs-<br>provision.</p>
      <p class="intro__note"><sup>*</sup>Nur gegen Vorlage des Flyers und Alleinauftrag!</p>
    </section>

    <p class="offer__value">2 %<sup>*</sup></p>
    <p class="offer__word">Provision</p>

    <div class="photo-dining" role="img" aria-label="Foto eines hellen Essbereichs mit Holztisch und Fensterblick ins Grüne"></div>

    <header class="valuation">
      <h2 class="valuation__title">IMMOBILIENBEWERTUNG</h2>
      <p class="valuation__region">für den Main-Kinzig-Kreis</p>
    </header>

    <section class="benefits">
      <p class="benefits__text">Wir helfen bei der Verwirklichung Ihres Wohntraums. Angebot gültig gegen Vorlage des Flyers.</p>
      <ul class="benefits__list">
        <li class="benefits__item">Übliche Maklerprovision 5,95 %</li>
        <li class="benefits__item">3,95 % bedeutet Alleinprovision oder geteilte Provision 1,97 %</li>
        <li class="benefits__item">Gilt ab ein Verkaufswert von 400.000,- Euro</li>
        <li class="benefits__item">Gültig bis 30. Dezember 2022</li>
      </ul>
    </section>

    <footer class="contact">
      <svg class="contact__phone-icon" width="38" height="38" viewBox="0 0 24 24" fill="#fff" aria-hidden="true">
        <path d="M6.6 10.8a15.1 15.1 0 0 0 6.6 6.6l2.2-2.2c.3-.3.7-.4 1-.2 1.1.4 2.3.6 3.6.6.6 0 1 .4 1 1V20c0 .6-.4 1-1 1A17 17 0 0 1 3 4c0-.6.4-1 1-1h3.5c.6 0 1 .4 1 1 0 1.3.2 2.5.6 3.6.1.3 0 .7-.2 1z"/>
        <path d="M14 3a7 7 0 0 1 7 7h-1.6A5.4 5.4 0 0 0 14 4.6zm0 3a4 4 0 0 1 4 4h-1.6A2.4 2.4 0 0 0 14 7.6z"/>
      </svg>
      <p class="contact__phone">06100 / 555210</p>
      <svg class="contact__pin" width="30" height="40" viewBox="0 0 24 32" aria-hidden="true">
        <path d="M12 0C5.4 0 0 5.2 0 11.7 0 20 12 32 12 32s12-12 12-20.3C24 5.2 18.6 0 12 0z" fill="#fff"/>
        <circle cx="12" cy="11.5" r="4.5" fill="#9dc544"/>
      </svg>
      <address class="contact__address">Velmora GmbH<br>Lindenweg 12<br>D-60000 Musterstadt</address>
    </footer>
  </main>
</body>
</html>
```